Tri-fold Brochure for Law Firm

Double-sided brochure to be folded into 6 sides tri-fold brochure for an estate planning special for new parents or parents-to-be. Brochure will be placed in classes for new parents/young parents.

Target Market(s)

New Parents Aged 24-34

Industry/Entity Type

Law Firm

Font styles to use
Serif

Requirements
Must have
• The information provided in the word document.
Nice to have
• Highlight the phrase "for New Parents."
• You may use the color scheme from our website:
• http://k47.9dw.sitevaultexample.com/

```html
<!DOCTYPE html>
<html lang="en">
<head>
<meta charset="utf-8">
<title>Hartwell Legal – Estate Planning Special for New Parents</title>
<link href="https://fonts.googleapis.com/css2?family=Playfair+Display:wght@400;700;900&family=Tinos:ital,wght@0,400;0,700;1,400&display=swap" rel="stylesheet">
<style>
  :root {
    --page-bg: #dcdcdc;
    --paper: #ffffff;
    --paper-grey: #ececec;
    --ink: #1e1e1e;
    --gold: #c9a13a;
    --gold-soft: #e8d7a8;
    --cover-dark: #0d0d0d;
    --copper: #a85f2a;
    --copper-dark: #6e3512;
    --muted: #b9b9b9;
  }
  * { box-sizing: border-box; margin: 0; padding: 0; }
  html, body { width: 1200px; height: 800px; overflow: hidden; }
  body {
    background: var(--page-bg);
    font-family: "Tinos", "Times New Roman", serif;
    color: var(--ink);
    display: flex; align-items: center; justify-content: center;
  }
  .brochure {
    width: 1020px; height: 760px;
    display: grid; grid-template-columns: repeat(3, 1fr);
    box-shadow: 0 10px 30px rgba(0,0,0,.18);
  }
  .panel { position: relative; overflow: hidden; }

  /* Panel 1 – attorney quote */
  .panel-quote { background: var(--paper); display: flex; flex-direction: column; align-items: center; }
  .portrait {
    margin-top: 60px; width: 170px; height: 170px; border-radius: 50%;
    border: 7px solid var(--gold);
    background: radial-gradient(circle at 50% 40%, #6b4a44 0%, #3a2a2a 55%, #4b4b4b 100%);
  }
  .quote { position: relative; width: 270px; margin-top: 40px; text-align: center; font-size: 14px; line-height: 1.3; }
  .quote-mark { position: absolute; font-family: "Playfair Display", serif; font-size: 64px; color: var(--muted); line-height: 1; }
  .quote-mark.open { left: -18px; top: -20px; }
  .quote-mark.close { right: -22px; bottom: -36px; }
  .quote-author { margin-top: 14px; color: var(--gold); font-size: 15px; text-align: center; }
  .gavel-photo {
    position: absolute; left: 0; right: 0; bottom: 0; height: 250px;
    background: linear-gradient(180deg, #ffffff 0%, #efe6d8 35%, #a0673a 65%, #6e4222 100%);
  }

  /* Panel 2 – contact */
  .panel-contact {
    background: linear-gradient(90deg, #dedede 0%, var(--paper-grey) 12%, #f7f7f7 60%, #e9e9e9 100%);
    display: flex; flex-direction: column; align-items: center; text-align: center;
  }
  .brand-mark { width: 60px; height: 60px; border-radius: 50%; background: var(--gold); margin-top: 250px; }
  .firm-name { margin-top: 14px; font-family: "Playfair Display", serif; font-weight: 700; font-size: 22px; letter-spacing: .5px; }
  .address { margin-top: 8px; font-size: 12.5px; line-height: 1.3; }
  .contact-list { margin-top: 12px; list-style: none; font-size: 12.5px; line-height: 2; }
  .contact-list li { display: flex; align-items: center; justify-content: center; gap: 6px; }
  .contact-list .pair { gap: 18px; }
  .contact-list svg { width: 11px; height: 11px; fill: var(--gold); }
  .divider { margin-top: 10px; width: 230px; height: 14px; }
  .terms { margin-top: 22px; width: 250px; font-size: 13px; line-height: 1.25; }

  /* Panel 3 – cover */
  .panel-cover { background: var(--cover-dark); color: #fff; }
  .cover-brand { display: flex; align-items: center; gap: 16px; padding: 30px 0 0 36px; }
  .cover-brand .brand-mark { margin: 0; width: 52px; height: 52px; }
  .cover-brand .name { font-family: "Playfair Display", serif; font-size: 19px; line-height: 1.15; letter-spacing: 1px; text-transform: uppercase; border-bottom: 1px solid var(--gold); padding-bottom: 4px; }
  .headline { text-align: center; font-family: "Playfair Display", serif; margin-top: 22px; line-height: 1; }
  .headline .main { font-weight: 900; font-size: 40px; display: block; }
  .headline .special { font-weight: 700; font-size: 22px; display: block; margin: 2px 0 2px 80px; }
  .headline .special small { font-size: 15px; }
  .headline .audience { font-weight: 700; font-size: 30px; display: block; text-transform: uppercase; letter-spacing: -.5px; }
  .scales-photo {
    position: absolute; left: 0; right: 0; top: 300px; height: 250px;
    background: radial-gradient(ellipse at 50% 45%, #a77c2e 0%, #4a3620 40%, #1b1410 75%), #1b1410;
  }
  .offer {
    position: absolute; left: 0; right: 0; top: 550px; height: 165px;
    background: linear-gradient(180deg, var(--copper) 0%, var(--copper-dark) 100%);
    text-align: center; padding-top: 18px;
  }
  .price { font-family: "Playfair Display", serif; font-weight: 900; font-size: 56px; display: inline-flex; align-items: center; gap: 6px; }
  .price small { font-size: 20px; font-weight: 700; line-height: .95; text-align: left; }
  .offer-note { font-family: "Playfair Display", serif; font-weight: 700; font-size: 17px; line-height: 1.2; margin-top: 4px; }
  .web-strip {
    position: absolute; left: 0; right: 0; bottom: 0; height: 45px; background: var(--cover-dark);
    display: flex; align-items: center; justify-content: center;
    font-family: "Playfair Display", serif; font-weight: 700; font-size: 15px; letter-spacing: 1px;
  }
</style>
</head>
<body>
<main class="brochure">

  <section class="panel panel-quote">
    <div class="portrait" role="img" aria-label="Portrait photograph of the attorney"></div>
    <blockquote class="quote">
      <span class="quote-mark open">&ldquo;</span>
      I’ve seen first-hand the problems created when a parent dies without a will. Young parents are least likely to think about estate planning, but having a plan for a guardian is most important when your children are small. I created our estate planning special to encourage new parents to start planning before it’s too late.
      <span class="quote-mark close">&rdquo;</span>
    </blockquote>
    <p class="quote-author">- Claire M. Hartwell, Esq.</p>
    <div class="gavel-photo" role="img" aria-label="Photograph of a wooden gavel resting on open law books"></div>
  </section>

  <section class="panel panel-contact">
    <div class="brand-mark" aria-hidden="true"></div>
    <h2 class="firm-name">HARTWELL LEGAL, LLC</h2>
    <p class="address">48 Elmwood Lane, Suite 310,<br>Greenfield, MD 21099</p>
    <ul class="contact-list">
      <li class="pair">
        <span><svg viewBox="0 0 10 10"><path d="M2 1l2 2-1 1c.5 1 1.5 2 3 3l1-1 2 2-1.5 1.5C4 9 1 6 .5 2.5z"/></svg> (410)-555-0142</span>
        <span><svg viewBox="0 0 10 10"><rect x="1" y="3" width="8" height="5" rx="1"/><rect x="3" y="1" width="4" height="2"/></svg> (410)-555-0187</span>
      </li>
      <li><svg viewBox="0 0 10 10"><path d="M1 2h8v6H1z M1 2l4 3 4-3" fill="none" stroke="#c9a13a" stroke-width="1"/></svg> claire@hartwell-legal.example</li>
      <li><svg viewBox="0 0 10 10"><circle cx="5" cy="5" r="4"/></svg> www.hartwell-legal.example</li>
    </ul>
    <svg class="divider" viewBox="0 0 230 14" aria-hidden="true"><path d="M2 12 Q115 -2 228 12" fill="none" stroke="#c9a13a" stroke-width="1"/></svg>
    <p class="terms">New Parent Estate Planning program ends 12/31/17. Special does not apply to individuals with over $1 million net worth or particularly complex plans. Special does not include drafting trusts. Available to Maryland residents only.</p>
  </section>

  <section class="panel panel-cover">
    <div class="cover-brand">
      <div class="brand-mark" aria-hidden="true"></div>
      <div class="name">Hartwell<br>Legal, LLC</div>
    </div>
    <h1 class="headline">
      <span class="main">Estate<br>Planning</span>
      <span class="special">Special <small>for</small></span>
      <span class="audience">New Parents</span>
    </h1>
    <div class="scales-photo" role="img" aria-label="Photograph of brass scales of justice and a gavel on a desk in a library"></div>
    <div class="offer">
      <div class="price">$750<small>per<br>couple</small></div>
      <p class="offer-note">For Parents-to-be And Parents<br>Of Children Under 5 Years Old.</p>
    </div>
    <div class="web-strip">WWW.HARTWELL-LEGAL.EXAMPLE</div>
  </section>

</main>
</body>
</html>
```